Complete Restaurant Branding Project

Bistro Velluto is looking for new ideas and designs for our various branded items.

You will be required to design the following items:

1) Staff Uniforms
2) Dine In Menu
3) Take Out Menu
4) Food Take Out Packaging
5) Take Out Bags
6) Beverage Take Out Cups
7) Dine in plates, coffee cups, mugs, etc...
8) Feel free to design any other brandable items related to our business

Please check our website to get a feel of our restaurant. Make sure to check the menu and the different dishes we offer to help you in the food packaging design and menu design. http://www.bistrovelluto-example.com/

We are open to new ideas, so we intentionally won't specify details such as materials, sizes, or shapes for any item.

We refined our logo in a contest a few days ago, the new logo is attached. Please don't use the logo from the website or any graphic elements from the website theme in your designs.

```html
<!DOCTYPE html>
<html lang="en">
<head>
<meta charset="utf-8">
<title>Bistro Velluto – Appetizers Menu</title>
<link rel="stylesheet" href="https://fonts.googleapis.com/css2?family=Libre+Baskerville:wght@400;700&family=Marcellus&display=swap">
<style>
  :root {
    --backdrop: #e4e4e6;
    --menu-brown: #8b3c1e;
    --menu-brown-dark: #7a3318;
    --cream: #f4e7cc;
    --cream-soft: #e9d6b4;
    --gold: #f3c232;
    --rule: rgba(243, 194, 50, 0.45);
  }
  * { box-sizing: border-box; margin: 0; padding: 0; }
  html, body {
    width: 1200px;
    height: 900px;
    overflow: hidden;
    background: var(--backdrop);
  }
  .canvas {
    position: relative;
    width: 1200px;
    height: 900px;
    display: flex;
    align-items: center;
    justify-content: center;
  }
  .menu-card {
    position: relative;
    width: 560px;
    height: 864px;
    padding: 30px 44px 0;
    background: radial-gradient(circle at 40% 30%, var(--menu-brown) 0%, var(--menu-brown-dark) 100%);
    color: var(--cream);
    font-family: "Libre Baskerville", Georgia, serif;
    overflow: hidden;
    box-shadow: 0 6px 20px rgba(0,0,0,0.18);
  }
  .brand {
    display: flex;
    align-items: center;
    justify-content: center;
    gap: 8px;
    font-family: "Libre Baskerville", Georgia, serif;
    font-weight: 700;
    font-size: 15px;
    color: var(--gold);
    letter-spacing: 0.04em;
  }
  .brand-dot {
    width: 12px;
    height: 12px;
    border-radius: 50%;
    background: var(--gold);
  }
  .menu-title {
    margin: 14px 0 18px;
    text-align: center;
    font-family: "Marcellus", Georgia, serif;
    font-weight: 400;
    font-size: 26px;
    letter-spacing: 0.06em;
    color: var(--cream);
  }
  .menu-list { list-style: none; }
  .menu-item {
    padding: 9px 0 9px;
    border-bottom: 1px solid var(--rule);
    width: 86%;
  }
  .menu-item:last-child { border-bottom: none; }
  .item-name {
    font-weight: 700;
    font-size: 16px;
    line-height: 1.25;
    color: var(--cream);
  }
  .item-desc {
    margin-top: 2px;
    font-size: 11px;
    line-height: 1.4;
    color: var(--cream-soft);
  }
  .ornament {
    position: absolute;
    right: -30px;
    bottom: -30px;
    width: 200px;
    height: 200px;
    border-radius: 50%;
    background: radial-gradient(circle, rgba(243,194,50,0.85) 0%, rgba(243,194,50,0.35) 55%, rgba(243,194,50,0) 72%);
  }
</style>
</head>
<body>
  <main class="canvas">
    <article class="menu-card">
      <header>
        <div class="brand"><span class="brand-dot"></span>Bistro Velluto</div>
        <h1 class="menu-title">APPETIZERS</h1>
      </header>
      <ul class="menu-list">
        <li class="menu-item">
          <h2 class="item-name">Velluto French Fries</h2>
          <p class="item-desc">Try them. They're irresistible !!!</p>
        </li>
        <li class="menu-item">
          <h2 class="item-name">Velluto Chili Fries</h2>
          <p class="item-desc">Velluto Fries covered with spicy chili, minced beef, cheddar cheese, sour cream and spring onions.</p>
        </li>
        <li class="menu-item">
          <h2 class="item-name">Onion Rings</h2>
          <p class="item-desc">Deep fried battered onion rings served with our barbecue sauce.</p>
        </li>
        <li class="menu-item">
          <h2 class="item-name">Rings'n Fries Combo</h2>
          <p class="item-desc">A combination of our onion rings and Velluto French Fries.</p>
        </li>
        <li class="menu-item">
          <h2 class="item-name">Chicken Wings</h2>
          <p class="item-desc">Choose your flavor Original, Barbecue, Teriyaki, Sweet and Sour.</p>
        </li>
        <li class="menu-item">
          <h2 class="item-name">French Bread Pizza</h2>
          <p class="item-desc">French bread baked with pizza sauce, mozzarella cheese and vegetables.</p>
        </li>
        <li class="menu-item">
          <h2 class="item-name">Velluto Sampler</h2>
          <p class="item-desc">French fries, French bread pizza, onion rings, and chicken wings.</p>
        </li>
        <li class="menu-item">
          <h2 class="item-name">Velluto Moutabak</h2>
          <p class="item-desc">Thin crust pizza folded, stuffed with minced beef, green onions and eggs.</p>
        </li>
        <li class="menu-item">
          <h2 class="item-name">Velluto Feta Moutabak</h2>
          <p class="item-desc">Thin crust pizza folded and stuffed with feta cheese, black olives and dill.</p>
        </li>
        <li class="menu-item">
          <h2 class="item-name">Garlic Bread</h2>
          <p class="item-desc">Served plain or with mozzarella cheese.</p>
        </li>
      </ul>
      <div class="ornament" role="img" aria-label="Yellow floral ornament in the corner"></div>
    </article>
  </main>
</body>
</html>
```